PIPE RELINING COMPANY NEEDS A NEW INFORMATIVE FLYER CREATED

We are a company that sells a service to residential homeowners (using a particular state of the art international product) and we need to refresh our A4 tri- fold flyer (z fold 6 pages). The layout needs to include pictures, heading and text boxes, but be simple and clean cut at the same time.

The front of the flyer must have the attached picture of the pipe under the house, logo and website.

This flyer is going to be given to clients and to leave with them when we quote for work.

Our colour scheme is black, white, red. A highlight colour if needed (in small amounts) could be 100% cyan and also a bright orange.

I have attached the copy of the text and this can be spread out throughout the brochure.

We are a professional and industry leading company so it needs to be professional, clean cut but with a modern edge.

Target Market(s)

HOMEOWNERS

Industry/Entity Type

It Company

Font styles to use
Sans Serif

Colors
ec1f27
ffffff
000000
f37122

Requirements
Must have
• PROFESSINAL, MODERN
• USE OF BLACK, RED AND WHITE - REFER LOGO
Should not have
• BE CLUTTERED

```html
<!DOCTYPE html>
<html lang="en">
<head>
<meta charset="utf-8">
<title>Seamline Pipe Relining – Tri-fold Brochure</title>
<link href="https://fonts.googleapis.com/css2?family=Roboto:wght@300;400;700;900&family=Roboto+Condensed:wght@400;700&display=swap" rel="stylesheet">
<style>
  :root{
    --red:#ec1f27;
    --black:#1a1a1a;
    --ink:#000000;
    --white:#ffffff;
    --grey:#444444;
    --stage:#e9e9e9;
  }
  *{box-sizing:border-box;margin:0;padding:0}
  html,body{width:1200px;height:1050px;overflow:hidden;background:var(--stage);font-family:"Roboto",sans-serif;color:var(--grey)}
  .spread{position:absolute;left:250px;width:700px;height:498px;background:var(--white);overflow:hidden;box-shadow:0 4px 14px rgba(0,0,0,.25)}
  .spread--inside{top:18px}
  .spread--outside{top:534px}
  .shapes{position:absolute;inset:0}
  .panel{position:absolute;top:0;height:498px}
  .body-text{font-size:6.6px;line-height:1.35;font-weight:300;color:var(--grey)}
  .body-text p{margin-bottom:7px}
  .on-dark{color:var(--white)}
  .red-head{color:var(--red);font-family:"Roboto Condensed",sans-serif;font-weight:700;font-size:7.4px;margin-bottom:5px}
  .bullets{list-style:none}
  .bullets li{position:relative;padding-left:9px;margin-bottom:7px}
  .bullets li::before{content:"";position:absolute;left:0;top:2px;width:4px;height:4px;border-radius:50%;background:var(--red)}
  .tag{position:absolute;left:0;top:186px;background:var(--red);color:var(--white);font-family:"Roboto Condensed",sans-serif;font-weight:700;font-size:8px;padding:5px 22px 5px 22px}
  .footer-url{position:absolute;bottom:0;height:44px;background:var(--red);color:var(--white);font-size:11px;letter-spacing:1.6px;display:flex;align-items:center;justify-content:center}
  .callout{position:absolute;left:236px;top:246px;width:226px;background:var(--black);color:var(--white);font-family:"Roboto Condensed",sans-serif;font-weight:700;font-size:7.2px;line-height:1.3;padding:8px 12px}
  .brand{display:flex;align-items:center;gap:6px;font-family:"Roboto",sans-serif;font-weight:900;color:var(--white);font-size:28px;letter-spacing:-.5px}
  .brand__mark{width:10px;height:10px;background:var(--red)}
  .photo{position:absolute;background:linear-gradient(180deg,#7aa6c9 0%,#c9c3b4 40%,#4f8a2c 62%,#5b3d28 100%)}
  .headline{text-align:center;font-family:"Roboto Condensed",sans-serif}
  .headline__lead{color:var(--red);font-size:16px}
  .headline__main{color:var(--ink);font-weight:700;font-size:22px;letter-spacing:.3px}
  .pill{display:inline-block;margin-top:8px;border:1px solid #555;border-radius:12px;padding:4px 10px;font-size:10.5px;font-weight:300;color:#333}
  .why-title{position:absolute;left:248px;top:30px;color:var(--white);font-family:"Roboto Condensed",sans-serif;font-weight:700;font-size:15px}
  .point-head{color:var(--red);font-size:7px;text-transform:uppercase;font-weight:400;margin-bottom:4px;line-height:1.3}
  .features{list-style:none;font-size:6.4px;font-weight:700;color:var(--white)}
  .features li{position:relative;padding-left:10px;margin-bottom:6px}
  .features li::before{content:"";position:absolute;left:0;top:1px;width:5px;height:5px;border-radius:50%;background:var(--red)}
  .call-band{position:absolute;left:0;top:192px;width:234px;height:150px;background:var(--red);text-align:center;color:var(--white)}
  .call-band__lead{margin-top:14px;font-size:10px;line-height:1.3;font-family:"Roboto Condensed",sans-serif}
  .call-band__phone{font-weight:900;font-size:31px;letter-spacing:1px;margin-top:2px}
  .scope{position:absolute;width:112px;height:112px;border-radius:50%;border:4px solid var(--white)}
  .contact{position:absolute;left:0;top:392px;width:234px;text-align:center;color:var(--white);font-size:10.5px;letter-spacing:1px;line-height:1.9}
</style>
</head>
<body>

<!-- Inside spread -->
<section class="spread spread--inside">
  <svg class="shapes" width="700" height="498" viewBox="0 0 700 498" aria-hidden="true">
    <polygon points="0,0 462,0 462,40 0,186" fill="#1a1a1a"/>
    <polygon points="240,118 462,0 462,100" fill="#ec1f27"/>
    <polygon points="0,186 462,40 462,100 240,118 0,230" fill="#f3f3f3"/>
    <rect x="462" y="0" width="238" height="92" fill="#1a1a1a"/>
    <line x1="236" y1="120" x2="236" y2="498" stroke="#dddddd" stroke-width="0.6"/>
  </svg>

  <div class="panel body-text on-dark" style="left:22px;top:18px;width:190px">
    <div class="red-head" style="font-size:7px">Which Problems Can Pipe Relining Repair?</div>
    <p>Pipe relining can repair broken, cracked or root infested pipes, pipes with missing sections and pipes that continually block.</p>
    <p>No matter if the pipes are vertical, horizontal or concealed, they all can be repaired. Sections of broken pipes can be relined, without having to replace the entire pipeline.</p>
  </div>

  <div class="tag">Patch Repair Process</div>

  <ul class="panel body-text bullets" style="left:22px;top:218px;width:196px">
    <li>Clean the line with a high pressure water jetter, and carry out a camera inspection to determine the exact location and cause of the problems.</li>
    <li>Prepare the liner. Cut the liner to the correct length, mix the appropriate amount of resin and impregnate the resin into the liner.</li>
    <li>Invert the liner into the pipe, inflate and then cure.</li>
    <li>A seamless, flexible liner is cut to length and filled with environmentally safe epoxy resin. The liner is then inverted into the existing host pipe and inflated using compressed air. Once the liner is fully cured with hot water, it is ready for use.</li>
    <li>The result is a completely new pipe inside the old. This pipe within a pipe is 100% water tight, stronger than PVC pipe, and has an increased flow rate compared to most existing pipes. Relined pipes have a life expectancy of 50 years and our installation work has a 25 year guarantee.</li>
  </ul>

  <div class="footer-url" style="left:0;width:234px">www.seamline.example</div>

  <div class="panel body-text" style="left:250px;top:120px;width:200px">
    <p>Sewers back up in properties due to ageing lines, misaligned joints, root infestation, calcification and ground movement, costing property owners thousands of dollars in damage to their homes and landscaping.</p>
    <p>Pipe relining eliminates the need for costly excavations to expose and replace this damaged pipework.</p>
    <p>Pipe Relining is the process of installing a new pipe within the old.</p>
  </div>

  <div class="callout">Why replace all of your drainage pipes when you can permanently repair the broken sections without destroying your environment</div>

  <div class="panel body-text" style="left:250px;top:302px;width:200px">
    <div class="red-head">What Does Pipe Relining Mean?</div>
    <p>Pipe relining is the method of repairing existing pipework from within the pipe itself. This is done by using the latest technology to insert a strong internal liner inside the existing pipe.</p>
    <p>During this process the resin impregnated side of the liner is pressed against the wall of the original host pipe at a specified pressure. This pressure ensure 100% resin contact and extrudes resin into all pipe joints, cracks and breaks ensuring no future tree root ingress or pipe movement is possible.</p>
    <p>Pipe relining can be undertaken in either short sectional repair, or long lengths utilising the inversion relining method.</p>
  </div>

  <div class="panel" style="left:462px;width:238px">
    <div class="brand" style="position:absolute;left:24px;top:28px"><span class="brand__mark"></span>Seamline</div>
    <div class="photo" role="img" aria-label="Photo of a house with a cut-away of the lawn showing tree roots growing into the sewer pipe underneath" style="left:0;top:92px;width:238px;height:248px"></div>
    <div class="headline" style="position:absolute;left:0;top:352px;width:238px">
      <div class="headline__lead">Repair Pipes Without</div>
      <div class="headline__main">DIGGING YOUR YARD</div>
      <div class="pill">Pipe Relining Sydney Wide 24/7</div>
    </div>
    <div class="footer-url" style="left:0;width:238px">www.seamline.example</div>
  </div>
</section>

<!-- Outside spread -->
<section class="spread spread--outside">
  <svg class="shapes" width="700" height="498" viewBox="0 0 700 498" aria-hidden="true">
    <rect x="0" y="0" width="234" height="498" fill="#1a1a1a"/>
    <polygon points="234,0 478,0 234,108" fill="#ec1f27"/>
    <polygon points="478,0 700,0 700,252 234,108" fill="#1a1a1a"/>
    <polygon points="234,108 700,252 700,300" fill="#f1f1f1"/>
  </svg>

  <div class="panel" style="left:0;width:234px">
    <div class="brand" style="position:absolute;left:34px;top:140px"><span class="brand__mark"></span>Seamline</div>
    <div class="call-band">
      <div class="call-band__lead">Call For Free Expert Advice<br>&amp; Great Rates On Pipe Relining</div>
      <div class="call-band__phone">5550 1234</div>
    </div>
    <div class="scope" role="img" aria-label="Camera inspection view inside a cracked clay sewer pipe" style="left:8px;top:280px;background:radial-gradient(circle,#1a0d08 12%,#7a4b38 45%,#c49a86 100%)"></div>
    <div class="scope" role="img" aria-label="Camera inspection view inside a newly relined pipe" style="left:118px;top:280px;background:radial-gradient(circle,#0c2a0a 12%,#3c9a2a 50%,#8fd46e 100%)"></div>
    <div class="contact">service@seamline.example<br>www.seamline.example</div>
  </div>

  <div class="why-title">WHY IT WORKS:</div>

  <div class="panel body-text" style="left:248px;top:158px;width:210px">
    <div class="point-head">Seamline uses epoxy resin not polyester or silicate resins.</div>
    <p>Why? Because epoxy resin does not shrink. Polyester and silicate resins can shrink in the pipe allowing tree roots to return.</p>
    <div class="point-head">Seamline inverts the liner instead of using a drag-in method.</div>
    <p>Why? Because this means that the resin has contact with the host pipe impregnating the cracks and joins the pipework. With the drag in method, the resin does not have contact with the host pipe and cannot impregnate the cracks and joins.</p>
    <div class="point-head">Seamline uses a German system called Lineflex.</div>
    <p>Why? Because it has been extensively tested in Europe and came out as the test winner in standard and extreme conditions based on all assessment criteria – effectiveness, density and load carrying capacity. Lineflex has a proven track record and been used to reline hundreds of kms throughout Europe.</p>
    <div class="point-head">Seamline provides a 25 year warranty</div>
    <p>Why? Because we understand the quality of the equipment and product and how we install it. We were one of the first to reline in NSW and are constantly carrying out research and development.</p>
  </div>

  <div class="panel" style="left:484px;top:16px;width:204px">
    <div style="color:var(--white);font-family:'Roboto Condensed',sans-serif;font-weight:700;font-size:8.6px;line-height:1.3;margin-bottom:5px">Provides a solution to the whole problem, not just temporary relief from the symptoms</div>
    <div class="red-head" style="font-size:6.8px;font-weight:400">What Does Pipe Relining Mean?</div>
    <ul class="features">
      <li>Permanent jointless liner</li>
      <li>50 years life expectancy</li>
      <li>Up front price</li>
      <li>Environmentally sound</li>
      <li>Eliminates structural disturbances</li>
      <li>Impervious to future root penetration</li>
      <li>Provides increased flow characteristics</li>
      <li>Suitable for industrial, residential and commercial applications</li>
    </ul>
  </div>

  <div class="panel body-text" style="left:484px;top:238px;width:204px">
    <div class="red-head" style="font-weight:400">Things You Should Know</div>
    <p>Knowledge &amp; Experience – We train other plumbers and have been doing it for over 10 years.</p>
    <p>We're An Owned &amp; Operated Business – We take great pride in our work. Our business is based on relationships not transactions.</p>
    <p>We Use the best in class pipe relining solution – We have sourced the best products and equipment from around the world and our Flowline product is from Germany.</p>
    <p>We have state of the art equipment – Our truck is customer designed and fully equipped with latest technology to carry out pipe relining.</p>
    <p>We're Fully licensed &amp; Insured – All of our technicians are fully licensed and qualified to complete the job. Our company is fully insured and are happy to provide you with documentation.</p>
    <p>After Sales Service – We don't forget about you after the job and as part of the warranty we carry out an annual camera inspection of the drainage.</p>
  </div>
</section>

</body>
</html>
```